Annual review for The Birchmoor Collective

The Birchmoor Collective is a small public relations agency in London specialising in corporate and public affairs. Most of our work is international and we have a strong connection to South Africa. We would like to prepare a short annual review for 2016. The review will serve as both a review of our activities in 2016, and as a credentials document. Content then will include:
1. An introduction to the business
2. Who we are
3. Projects and clients undertaken in 2016
4. News and views
We imagine it will be used mostly as a pdf but would like it to be suitable for print. We envisage it to be about 8 pages long. The design look and feel should convey a business, while small, of stature. We shall include some of our client logos but we would welcome the use of some photography / imagery to have visual impact (although we don't have very much of our own!). The corporate look and feel is white, grey and black.

Industry/Entity Type

Public Relation

Font styles to use
Sans Serif

Requirements
Must have
• My project must convey a business with flair and gravitas, that punches above its weight.
Nice to have
• Thoughtful use of imagery.

```html
<!DOCTYPE html>
<html lang="en">
<head>
<meta charset="utf-8">
<title>The Birchmoor Collective — Annual Review 2016 Cover</title>
<link href="https://fonts.googleapis.com/css2?family=Open+Sans:wght@400;700&display=swap" rel="stylesheet">
<style>
  :root {
    --paper: #ffffff;
    --band-grey: #6b6c6e;
    --brand-grey: #5f6062;
    --ink-light: #ffffff;
    --web-grey: #55565a;
  }
  html, body {
    margin: 0;
    padding: 0;
    width: 1200px;
    height: 849px;
    overflow: hidden;
    background: var(--paper);
    font-family: "Open Sans", Arial, sans-serif;
  }
  .spread {
    position: relative;
    width: 1200px;
    height: 849px;
    background: var(--paper);
  }
  .brand {
    position: absolute;
    display: flex;
    align-items: center;
    gap: 12px;
    color: var(--brand-grey);
    font-weight: 700;
    font-size: 23px;
    letter-spacing: -0.01em;
    white-space: nowrap;
  }
  .brand-dot {
    width: 30px;
    height: 30px;
    border: 2px solid var(--brand-grey);
    border-radius: 50%;
    box-sizing: border-box;
  }
  .brand--back { left: 135px; top: 126px; }
  .brand--front { left: 736px; top: 679px; }

  .contact-band {
    position: absolute;
    left: 0;
    top: 272px;
    width: 600px;
    height: 271px;
    background: var(--band-grey);
  }
  .office {
    position: absolute;
    left: 0;
    width: 606px;
    margin: 0;
    text-align: center;
    color: var(--ink-light);
    font-size: 12px;
    line-height: 14.5px;
    font-style: normal;
  }
  .office--london { top: 81px; }
  .office--paris { top: 153px; }

  .cover-photo {
    position: absolute;
    left: 600px;
    top: 0;
    width: 600px;
    height: 543px;
    background:
      linear-gradient(180deg, rgba(0,0,0,0) 0, rgba(0,0,0,0) 272px, rgba(40,40,40,0.35) 272px, rgba(40,40,40,0.35) 543px),
      linear-gradient(180deg, #bdbdbd 0%, #8e8e8e 12%, #5a5a5a 22%, #6f6f6f 38%, #9c9c9c 50%, #8a8a8a 65%, #7a7a7a 80%, #5e5e5e 100%);
  }
  .cover-title {
    position: absolute;
    left: 600px;
    top: 400px;
    width: 600px;
    margin: 0;
    text-align: center;
    color: var(--ink-light);
    font-weight: 700;
    font-size: 16px;
    letter-spacing: 0.45em;
    padding-left: 0.45em;
    box-sizing: border-box;
  }
  .website {
    position: absolute;
    left: 184px;
    top: 676px;
    margin: 0;
    color: var(--web-grey);
    font-size: 13.5px;
    letter-spacing: 0.2em;
  }
</style>
</head>
<body>
  <main class="spread">
    <div class="brand brand--back"><span class="brand-dot"></span>The Birchmoor Collective</div>

    <section class="contact-band">
      <address class="office office--london">The Birchmoor Collective<br>14 Marlow Lane<br>London W1K 3PQ</address>
      <address class="office office--paris">The Birchmoor Collective<br>42 rue des Lilas<br>75011 Paris</address>
    </section>

    <p class="website">www.birchmoorcollective.com</p>

    <div class="cover-photo" role="img" aria-label="Black and white photograph of a rocky cape headland and sandy beach beside the sea under a cloudy sky"></div>
    <h1 class="cover-title">ANNUAL REVIEW | 2016</h1>

    <div class="brand brand--front"><span class="brand-dot"></span>The Birchmoor Collective</div>
  </main>
</body>
</html>
```